Winery Website for Thorn Mere Cellars.

We are working with ThornMere Cellars. They are a winery and in need of a new website design.

Some sites to use for inspiration:

https://calvettaplum.com
https://vomelo.com
https://plainbarnvino.com
http://www.quentavineyard.com
https://www.ravinagrapes.com

Thank you for taking the time to consider designing a website for us. We are web developers based in Stockton, CA, USA. Most of our projects go through the same process. Understanding this process may help you win a project with us. We custom-code all of our websites in-house. We don’t have any requirements as to what tools you use for your design, but we prefer Figma files. For any design that we label as four-stars, we send it to the client for review. The client picks the final design they want us to use. Once we complete this process, we will continue to show additional clients all the four-star sites and purchase them later. Your designs will have multiple chances to sell. For better chances of success, we ask that you follow these guidelines.

IMAGES:
If you use any images or icons in the design, we ask that you have a link to the asset so we can purchase the image/icon. Most of the designs we submit do not have the customer’s images on them unless they have some great images. Be creative; show us the feeling you are trying to portray with your image choices. Use any royalty-free site you choose. We subscribe to Pixtrel and mainly use their images, but we can purchase images outside of Pixtrel.

PLEASE NOTE: we will not submit designs to clients with watermarks on the images.

FONTS:
We ask that you identify the fonts used in the design. This can be done in a message if you want. We typically use Zanbo Type and Pixtrel Type.

CONTENT:
We're always open to different content and ideas. We often submit designs with stock images so the client can see our vision. We typically take pictures after the website launch to use their images with our vision. Lorem Ipsum is fine for paragraphs, but we ask that you write the headers in correct English. We want to be able to show the vision and identify the sections of the website.

INSPIRATION:
We typically add a couple of links in the brief of websites we like to help you get started in your design.

REVISIONS:
We do not often ask for revisions of the designs unless we see something in the design that may not appeal to the client. If there are slight changes that we want to make, we do that in the development process.

FEEDBACK:
We rarely give feedback on designs during the design process. We are working on many website projects and do not have the time to provide feedback. We usually respond if your request is well thought out and asks specific questions, but a note asking “feedback, please” usually goes unanswered.

```html
<!DOCTYPE html>
<html lang="en">
<head>
<meta charset="utf-8">
<title>ThornMere Cellars</title>
<link href="https://fonts.googleapis.com/css2?family=Quicksand:wght@500;600;700&family=Poppins:wght@400;500;600&display=swap" rel="stylesheet">
<style>
:root{
  --blue:#2f6fd9;
  --ink:#111418;
  --muted:#3a3f47;
  --white:#ffffff;
  --line:#d9dde3;
  --hero-a:#2a1a12;
  --hero-b:#7a4a2a;
  --wine:#6b1a22;
  --gold:#c98a3c;
}
*{box-sizing:border-box;margin:0;padding:0}
html,body{width:1200px;height:3084px;overflow:hidden;background:var(--white)}
body{font-family:"Poppins",sans-serif;color:var(--ink);position:relative}
h1,h2,h3{font-family:"Quicksand",sans-serif;font-weight:600}
.btn{display:inline-block;background:var(--blue);color:var(--white);font-size:13px;font-weight:500;padding:9px 16px;border-radius:3px}

/* header */
.site-header{position:absolute;top:0;left:0;width:1200px;height:112px;display:flex;align-items:center;padding:0 56px}
.brand{display:flex;align-items:center;gap:10px;font-family:"Quicksand",sans-serif;font-weight:700;font-size:24px;color:var(--ink)}
.brand-dot{width:14px;height:14px;border-radius:50%;background:var(--blue)}
.main-nav{display:flex;gap:30px;margin-left:250px;font-size:15px;font-weight:500}
.header-icons{margin-left:auto;display:flex;gap:12px}
.header-icons span{width:28px;height:28px;border-radius:50%;background:var(--blue);display:flex;align-items:center;justify-content:center}

/* hero */
.hero{position:absolute;top:112px;left:0;width:1200px;height:488px;background:linear-gradient(90deg,var(--hero-a) 0%,#4a2f1e 45%,var(--hero-b) 75%,#3a2516 100%)}
.hero-copy{position:absolute;left:56px;top:118px;color:var(--white);width:560px}
.hero-copy h1{font-size:66px;line-height:1.05;font-weight:600}
.hero-copy p{font-size:13px;line-height:1.5;margin:14px 0 18px;width:540px}
.hero-next{position:absolute;right:48px;top:236px;width:30px;height:30px;border-radius:50%;background:var(--white);display:flex;align-items:center;justify-content:center}

/* categories */
.categories{position:absolute;top:656px;left:56px;width:1088px;display:flex;gap:14px}
.category{position:relative;flex:1;height:246px}
.category .btn{position:absolute;left:20px;bottom:16px;padding:7px 14px;font-size:12px}
.cat-red{background:linear-gradient(135deg,#8a5a3e,#d7b59a)}
.cat-sparkling{background:linear-gradient(135deg,#e9e6df,#b9b3a2)}
.cat-rose{background:linear-gradient(135deg,#d88a2a,#7a3b1a)}

/* about */
.about{position:absolute;top:968px;left:0;width:1200px;height:460px;background:linear-gradient(90deg,#6a4a30 0%,#9b7a52 35%,#4a3422 60%,#2e2016 100%)}
.about-copy{position:absolute;left:656px;top:52px;width:480px;color:var(--white)}
.about-copy h2{font-size:66px;line-height:1.1}
.about-copy p{font-size:13px;line-height:1.5;margin-top:14px}
.about-copy .btn{margin-top:18px}

/* collections */
.collections{position:absolute;top:1480px;left:56px;width:1088px}
.collections h2{font-size:64px}
.slider-arrows{position:absolute;right:0;top:16px;display:flex;gap:8px}
.slider-arrows span{width:32px;height:32px;border:1.5px solid var(--ink);display:flex;align-items:center;justify-content:center}
.products{display:flex;gap:58px;margin-top:44px}
.product{width:324px}
.product-img{height:316px}
.img-red{background:radial-gradient(circle at 40% 50%,#5a0f18,#f3f1ef 70%)}
.img-white{background:radial-gradient(circle at 45% 55%,#e7c45a,#fbfaf7 70%)}
.img-rose{background:radial-gradient(circle at 45% 55%,#e79aa8,#fdf7f8 70%)}
.product h3{font-family:"Poppins",sans-serif;font-size:15px;font-weight:600;margin-top:24px}
.product p{font-size:13px;line-height:1.45;color:var(--muted);margin:8px 0 14px;width:300px}

/* find */
.find{position:absolute;top:2148px;left:0;width:1200px;height:592px;background:linear-gradient(180deg,#7d8fa3 0%,#9aa49e 35%,#4f6a3a 70%,#2e3a22 100%)}
.find h2{position:absolute;left:56px;top:40px;font-size:64px;line-height:1.12;color:var(--white);width:600px}
.find-side{position:absolute;left:752px;top:76px;width:390px;color:var(--white)}
.find-side p{font-size:13px;line-height:1.4}
.search{margin-top:16px;height:46px;background:var(--white);display:flex;align-items:center;justify-content:space-between;padding:0 18px;color:#777;font-size:13px}
.map{position:absolute;left:56px;top:254px;width:556px;height:290px;background:linear-gradient(135deg,#eef0ea,#dfe6ee)}

/* footer */
.site-footer{position:absolute;top:2740px;left:0;width:1200px;height:344px}
.footer-brand{position:absolute;left:56px;top:66px}
.footer-brand .brand{font-size:34px}
.footer-brand p{font-size:13px;line-height:1.5;width:300px;margin-top:54px}
.footer-col{position:absolute;top:60px}
.footer-col h4{font-size:13px;font-weight:500;color:var(--blue);margin-bottom:12px}
.footer-col li{list-style:none;font-size:13px;margin-bottom:9px;padding-left:12px;position:relative}
.footer-col li::before{content:"";position:absolute;left:0;top:8px;width:4px;height:4px;border-radius:50%;background:var(--ink)}
.col-links{left:492px}.col-wines{left:708px}
.col-news{left:936px;width:210px}
.col-news p{font-size:13px;line-height:1.4}
.email{margin-top:20px;border-bottom:1px solid var(--ink);display:flex;justify-content:space-between;font-size:12px;padding-bottom:6px}
.socials{display:flex;gap:8px;margin-top:20px}
.socials span{width:22px;height:22px;border-radius:50%;background:var(--ink)}
.copyright{position:absolute;left:0;top:264px;width:1200px;border-top:1px solid var(--line);text-align:center;font-size:12px;padding-top:28px}
</style>
</head>
<body>

<header class="site-header">
  <div class="brand"><span>ThornMere Cellars</span><span class="brand-dot"></span></div>
  <nav class="main-nav"><span>Home</span><span>About Us</span><span>Wines</span><span>Visit Us</span><span>Contact</span></nav>
  <div class="header-icons">
    <span><svg width="14" height="14" viewBox="0 0 14 14"><circle cx="7" cy="4.5" r="2.6" fill="none" stroke="#fff" stroke-width="1.5"/><path d="M2 13c0-3 2.5-4.5 5-4.5s5 1.5 5 4.5" fill="none" stroke="#fff" stroke-width="1.5"/></svg></span>
    <span><svg width="14" height="14" viewBox="0 0 14 14"><path d="M1 2h2l1.6 7h7L13 4H4" fill="none" stroke="#fff" stroke-width="1.5"/><circle cx="5.5" cy="12" r="1" fill="#fff"/><circle cx="10.5" cy="12" r="1" fill="#fff"/></svg></span>
  </div>
</header>

<section class="hero" role="img" aria-label="Wine bottles and a filled glass on a barrel in a stone cellar arch">
  <div class="hero-copy">
    <h1>Discover handcrafted wines</h1>
    <p>Discover handcrafted wines born from the unique terroir of our coastal vineyards. Experience the passion in every bottle.</p>
    <span class="btn">Explore Our Wines</span>
  </div>
  <span class="hero-next"><svg width="10" height="10" viewBox="0 0 10 10"><path d="M3 1l4 4-4 4" fill="none" stroke="#111" stroke-width="1.6"/></svg></span>
</section>

<section class="categories">
  <div class="category cat-red" role="img" aria-label="Glasses of white wine with grapes on a wooden table"><span class="btn">White Wine</span></div>
  <div class="category cat-sparkling" role="img" aria-label="Sparkling wine bottle and glasses in a bright room"><span class="btn">Sparkling Wine</span></div>
  <div class="category cat-rose" role="img" aria-label="Red wine bottle and glass in a sunset vineyard"><span class="btn">Red Wine</span></div>
</section>

<section class="about" role="img" aria-label="Oak barrel, red wine glasses and grapes before a vineyard">
  <div class="about-copy">
    <h2>About Us</h2>
    <p>At ThornMere Cellars, winemaking is more than a craft – it's a legacy. Founded by Mr. Halden in 1989 with a vision to capture the distinct character of our coastal region, our family-owned winery blends time-honored techniques with innovative approaches.</p>
    <p>Discover the taste of our land, nurtured by the sea breeze and sun-drenched slopes.</p>
    <span class="btn">Learn More ThornMere</span>
  </div>
</section>

<section class="collections">
  <h2>Wine Collections</h2>
  <div class="slider-arrows">
    <span><svg width="10" height="10" viewBox="0 0 10 10"><path d="M7 1L3 5l4 4" fill="none" stroke="#111" stroke-width="1.6"/></svg></span>
    <span><svg width="10" height="10" viewBox="0 0 10 10"><path d="M3 1l4 4-4 4" fill="none" stroke="#111" stroke-width="1.6"/></svg></span>
  </div>
  <div class="products">
    <article class="product">
      <div class="product-img img-red" role="img" aria-label="Red wine bottle with a filled glass and grapes"></div>
      <h3>Red Wine</h3>
      <p>Rich and complex, our coastal red wines showcase the depth of flavor</p>
      <span class="btn">Shop Now</span>
    </article>
    <article class="product">
      <div class="product-img img-white" role="img" aria-label="White wine bottle and glass with cheese board"></div>
      <h3>White Wine</h3>
      <p>Our vibrant rosé captures the essence of the coast</p>
      <span class="btn">Shop Now</span>
    </article>
    <article class="product">
      <div class="product-img img-rose" role="img" aria-label="Rosé wine bottle and glasses with pink roses"></div>
      <h3>Rose Wine</h3>
      <p>our white wines highlight the pure fruit and refreshing acidity of our coastal</p>
      <span class="btn">Shop Now</span>
    </article>
  </div>
</section>

<section class="find" role="img" aria-label="Vineyard with wine bottle and barrel beneath distant mountains">
  <h2>Find ThornMere Wines Near You</h2>
  <div class="find-side">
    <p>Need ThornMere & Stockists? Use this page to find stores near you.</p>
    <div class="search"><span>Search Here</span><svg width="14" height="14" viewBox="0 0 14 14"><circle cx="6" cy="6" r="4.5" fill="none" stroke="#111" stroke-width="1.5"/><path d="M9.5 9.5L13 13" stroke="#111" stroke-width="1.5"/></svg></div>
  </div>
  <div class="map" role="img" aria-label="Street map with store location pins"></div>
</section>

<footer class="site-footer">
  <div class="footer-brand">
    <div class="brand"><span>ThornMere Cellars</span><span class="brand-dot"></span></div>
    <p>Discover the taste of our land, nurtured by the sea breeze and sun-drenched slopes</p>
  </div>
  <div class="footer-col col-links">
    <h4>Quick Links</h4>
    <ul><li>Home</li><li>About Us</li><li>Wines</li><li>Visit Us</li><li>Contact</li></ul>
  </div>
  <div class="footer-col col-wines">
    <h4>Our Wines</h4>
    <ul><li>Red Wine</li><li>White Wine</li><li>Rose Wine</li><li>Sparkling Wine</li><li>Shop</li></ul>
  </div>
  <div class="footer-col col-news">
    <h4>Join our mailing list &amp; earn</h4>
    <p>15% off your first order</p>
    <div class="email"><span>Enter your mail</span><span>›</span></div>
    <div class="socials"><span></span><span></span><span></span><span></span></div>
  </div>
  <div class="copyright">Copyright © 2025 ThornMere Cellars. Crafted with Passion. All Rights Reserved.</div>
</footer>

</body>
</html>
```